Exciting New Health Brand. Needs packaging design

We need a label and packaging design for a US based colloidal Silver water product due to launch shortly.
we like the vibe and feel of this: https://www.shopvarlo.example/Pure-Brightwell-Dropper-Top-Regal-Tonic/dp/K48TRW2MPL/ref=sr_1_1_sspa?ie=UTF8&qid=1520284298&sr=8-1-spons&keywords=regal+tonic+colloidal+tonic&psc=1 though would need to make it look different

Target Market(s)

people who like natural health, and alternative health such as yoga, reiki etc

Industry/Entity Type

Health And Wellness

Font styles to use
Other font styles liked:
• open minded

Colors

Designer to choose colors to be used in the design.

Requirements
Must have
• Vibrant feel.Brand name is fernwell vitals
Nice to have
• quite open minded
Should not have
• mustn't have cheap animated look

```html
<!DOCTYPE html>
<html lang="en">
<head>
<meta charset="utf-8">
<title>Fernwell Vitals – Immune Support Packaging</title>
<link rel="stylesheet" href="https://fonts.googleapis.com/css2?family=Cinzel:wght@600;700&family=PT+Sans+Narrow:wght@400;700&display=swap">
<style>
  :root {
    --backdrop-light: #eeeeef;
    --backdrop-dark: #c9cacc;
    --silver-light: #f3f4f6;
    --silver-mid: #c3c7cd;
    --silver-dark: #9ea3aa;
    --ocean-deep: #0d4f88;
    --ocean: #2a7dbf;
    --ocean-light: #5fa6d8;
    --gold: #e3a338;
    --gold-light: #f8d47e;
    --ink: #161a22;
    --navy: #1d2a44;
    --white: #ffffff;
  }
  html, body {
    margin: 0;
    width: 1200px;
    height: 1200px;
    overflow: hidden;
  }
  body {
    background: radial-gradient(ellipse at 50% 40%, var(--backdrop-light), var(--backdrop-dark));
  }
  .packaging { display: block; width: 1200px; height: 1200px; }
  .brand-name { font-family: "Cinzel", serif; font-weight: 700; fill: var(--ink); }
  .condensed { font-family: "PT Sans Narrow", sans-serif; }
  .headline { font-weight: 700; fill: var(--white); font-size: 40px; letter-spacing: 0.5px; }
  .pill-label { font-weight: 700; fill: var(--navy); }
  .rank-number { font-family: "PT Sans Narrow", sans-serif; font-weight: 700; fill: var(--ink); font-size: 54px; }
  .rank-caption { font-family: "PT Sans Narrow", sans-serif; font-weight: 700; fill: var(--navy); font-size: 14px; }
  .strength { font-family: "PT Sans Narrow", sans-serif; font-weight: 700; fill: var(--white); font-size: 36px; }
  .side-brand { font-family: "Cinzel", serif; font-weight: 700; fill: var(--ink); font-size: 13px; }
  .feature-title { font-family: "PT Sans Narrow", sans-serif; font-weight: 700; fill: var(--ink); font-size: 10px; }
  .feature-text { font-family: "PT Sans Narrow", sans-serif; fill: #2b3038; font-size: 8px; }
  .panel-text { font-family: "PT Sans Narrow", sans-serif; fill: var(--white); font-size: 9px; opacity: 0.9; }
</style>
</head>
<body>
<svg class="packaging" viewBox="0 0 1200 1200" xmlns="http://www.w3.org/2000/svg">
  <defs>
    <linearGradient id="silverSheen" x1="0" y1="0" x2="1" y2="0">
      <stop offset="0" stop-color="var(--silver-dark)"/>
      <stop offset="0.45" stop-color="var(--silver-light)"/>
      <stop offset="0.6" stop-color="var(--white)"/>
      <stop offset="1" stop-color="var(--silver-mid)"/>
    </linearGradient>
    <linearGradient id="sideSilver" x1="0" y1="0" x2="1" y2="0">
      <stop offset="0" stop-color="#b8bcc2"/>
      <stop offset="1" stop-color="#d6d9dd"/>
    </linearGradient>
    <linearGradient id="oceanFill" x1="0" y1="0" x2="0" y2="1">
      <stop offset="0" stop-color="var(--ocean)"/>
      <stop offset="0.35" stop-color="var(--ocean-light)"/>
      <stop offset="0.7" stop-color="#1f6aa8"/>
      <stop offset="1" stop-color="var(--ocean-deep)"/>
    </linearGradient>
    <linearGradient id="goldFill" x1="0" y1="0" x2="0" y2="1">
      <stop offset="0" stop-color="var(--gold-light)"/>
      <stop offset="1" stop-color="var(--gold)"/>
    </linearGradient>
    <linearGradient id="topStrip" x1="0" y1="0" x2="1" y2="0">
      <stop offset="0" stop-color="var(--ocean-deep)"/>
      <stop offset="0.5" stop-color="#9cc4e6"/>
      <stop offset="1" stop-color="var(--ocean-deep)"/>
    </linearGradient>
    <radialGradient id="emblemFill" cx="0.4" cy="0.35" r="0.8">
      <stop offset="0" stop-color="var(--white)"/>
      <stop offset="1" stop-color="var(--silver-mid)"/>
    </radialGradient>
    <path id="headlineArc" d="M535,432 Q695,382 855,432"/>
  </defs>

  <!-- Side panel -->
  <g class="side-panel">
    <rect x="320" y="80" width="190" height="520" fill="url(#sideSilver)"/>
    <rect x="320" y="80" width="190" height="22" fill="url(#topStrip)"/>
    <text class="side-brand" x="415" y="140" text-anchor="middle">FERNWELL</text>
    <text class="side-brand" x="415" y="158" text-anchor="middle">VITALS</text>

    <g class="feature" transform="translate(0,0)">
      <circle cx="352" cy="240" r="27" fill="var(--gold)"/>
      <circle cx="352" cy="240" r="22" fill="var(--ocean-deep)" role="img" aria-label="Pure silver icon"/>
      <text class="feature-title" x="387" y="222">PURE SILVER</text>
      <text class="feature-text" x="387" y="236">Fine particles in pure water</text>
      <text class="feature-text" x="387" y="247">for calm, steady daily wellness</text>
      <text class="feature-text" x="387" y="258">made with care in the USA</text>
    </g>
    <g class="feature" transform="translate(0,100)">
      <circle cx="352" cy="240" r="27" fill="var(--gold)"/>
      <circle cx="352" cy="240" r="22" fill="var(--ocean-deep)" role="img" aria-label="Daily defense icon"/>
      <text class="feature-title" x="387" y="222">DAILY DEFENSE</text>
      <text class="feature-text" x="387" y="236">Fine particles in pure water</text>
      <text class="feature-text" x="387" y="247">for calm, steady daily wellness</text>
      <text class="feature-text" x="387" y="258">made with care in the USA</text>
    </g>
    <g class="feature" transform="translate(0,200)">
      <circle cx="352" cy="240" r="27" fill="var(--gold)"/>
      <circle cx="352" cy="240" r="22" fill="var(--ocean-deep)" role="img" aria-label="Gentle formula icon"/>
      <text class="feature-title" x="387" y="222">GENTLE</text>
      <text class="feature-text" x="387" y="236">Fine particles in pure water</text>
      <text class="feature-text" x="387" y="247">for calm, steady daily wellness</text>
      <text class="feature-text" x="387" y="258">made with care in the USA</text>
    </g>
    <g class="feature" transform="translate(0,300)">
      <circle cx="352" cy="240" r="27" fill="var(--gold)"/>
      <circle cx="352" cy="240" r="22" fill="var(--ocean-deep)" role="img" aria-label="Everyday use icon"/>
      <text class="feature-title" x="387" y="222">EVERYDAY USE</text>
      <text class="feature-text" x="387" y="236">Fine particles in pure water</text>
      <text class="feature-text" x="387" y="247">for calm, steady daily wellness</text>
      <text class="feature-text" x="387" y="258">made with care in the USA</text>
    </g>

    <rect x="320" y="600" width="190" height="520" fill="var(--ocean-deep)"/>
    <g class="directions">
      <text class="panel-text" x="335" y="660">Take one dropper daily, or as</text>
      <text class="panel-text" x="335" y="673">directed by your health advisor.</text>
      <text class="panel-text" x="335" y="686">Shake gently before each use and</text>
      <text class="panel-text" x="335" y="699">hold under the tongue for thirty</text>
      <text class="panel-text" x="335" y="712">seconds before you swallow. Keep</text>
      <text class="panel-text" x="335" y="725">out of reach of young children.</text>

      <text class="panel-text" x="335" y="865">Store in a cool, dark place away</text>
      <text class="panel-text" x="335" y="878">from direct light. Do not freeze.</text>
      <text class="panel-text" x="335" y="891">Keep the cap tightly closed.</text>

      <text class="panel-text" x="335" y="930">These statements have not been</text>
      <text class="panel-text" x="335" y="943">evaluated by the FDA. Not meant</text>
      <text class="panel-text" x="335" y="956">to diagnose or treat disease.</text>

      <line x1="330" y1="1040" x2="500" y2="1040" stroke="var(--white)" stroke-opacity="0.4"/>
      <text class="panel-text" x="335" y="1062">Made in the USA with purified water</text>
      <text class="panel-text" x="335" y="1075">and ten ppm fine colloidal silver.</text>
      <line x1="330" y1="1092" x2="500" y2="1092" stroke="var(--white)" stroke-opacity="0.4"/>
    </g>
  </g>

  <!-- Front panel -->
  <g class="front-panel">
    <rect x="510" y="80" width="370" height="280" fill="url(#silverSheen)"/>
    <rect x="510" y="80" width="370" height="22" fill="url(#topStrip)"/>
    <text class="brand-name" x="695" y="200" text-anchor="middle" font-size="50">FERNWELL</text>
    <text class="brand-name" x="695" y="268" text-anchor="middle" font-size="50">VITALS</text>

    <g class="ocean-photo" role="img" aria-label="Photograph of a rolling blue ocean wave">
      <path d="M510,350 Q695,318 880,350 L880,1120 L510,1120 Z" fill="url(#oceanFill)"/>
    </g>
    <path d="M510,350 Q695,318 880,350" fill="none" stroke="var(--gold)" stroke-width="8"/>

    <rect class="center-strip" x="652" y="350" width="86" height="110" fill="var(--navy)" fill-opacity="0.35"/>
    <rect class="center-strip" x="652" y="460" width="86" height="520" fill="var(--white)" fill-opacity="0.28"/>

    <text class="condensed headline"><textPath href="#headlineArc" startOffset="50%" text-anchor="middle">IMMUNE SUPPORT</textPath></text>
    <path d="M565,452 Q695,420 825,452" fill="none" stroke="var(--white)" stroke-opacity="0.7" stroke-width="1.5"/>

    <circle class="emblem-placeholder" cx="695" cy="575" r="56" fill="url(#emblemFill)" role="img" aria-label="Bio active emblem"/>

    <rect x="600" y="700" width="190" height="50" rx="25" fill="url(#goldFill)"/>
    <text class="condensed pill-label" x="695" y="735" text-anchor="middle" font-size="29">DROPPER-TOP</text>

    <path d="M510,925 L560,925 Q615,822 695,822 Q775,822 830,925 L880,925" fill="none" stroke="var(--white)" stroke-opacity="0.6" stroke-width="1.5"/>
    <circle cx="695" cy="880" r="64" fill="none" stroke="var(--white)" stroke-opacity="0.7" stroke-width="1.5"/>
    <circle cx="695" cy="880" r="54" fill="var(--white)" fill-opacity="0.2"/>
    <path d="M641,892 A54,54 0 0 0 749,892 Z" fill="url(#goldFill)"/>
    <text class="rank-number" x="695" y="878" text-anchor="middle">1</text>
    <text class="rank-caption" x="695" y="911" text-anchor="middle">SELLING SILVER</text>
    <text class="rank-caption" x="695" y="926" text-anchor="middle">IN THE U.S</text>

    <text class="strength" x="695" y="1016" text-anchor="middle">10 PPM</text>

    <rect x="535" y="1030" width="320" height="74" rx="37" fill="url(#silverSheen)"/>
    <circle cx="561" cy="1067" r="7" fill="var(--gold-light)"/>
    <circle cx="829" cy="1067" r="7" fill="var(--gold-light)"/>
    <text class="condensed pill-label" x="695" y="1062" text-anchor="middle" font-size="26">DIETARY SUPPLEMENT</text>
    <text class="condensed" x="695" y="1092" text-anchor="middle" font-size="24" fill="var(--navy)">10 ppm/8fl.oz / 236ml</text>
  </g>
</svg>
</body>
</html>
```